Bref créative
Norland Equity Partners
Investing
Professional
Tom Radcliffe
President
728 Maplewood Ave. Suite 310
Oak Terrace, CA 90418
tom@NorlandEquityPartners.com
www.NorlandEquityPartners.com
We want our logo to be the main component of the card. Have fun and let me see what you got!
Feel free to try 1 or 2 sided card ideas.
Can use other fonts besides the logo font if you desire.

```html
<!DOCTYPE html>
<html lang="en">
<head>
<meta charset="utf-8">
<title>Norland Equity Partners – Stationery</title>
<link rel="stylesheet" href="https://fonts.googleapis.com/css2?family=Source+Sans+3:wght@400;600;700&display=swap">
<style>
  :root {
    --backdrop: #7190ee;
    --paper: #ffffff;
    --ink: #1c1c1c;
    --brand-red: #e5231b;
    --muted: #444444;
    --faint: #f3ecea;
    --flap: #151515;
    --lining: #3a3a3a;
  }
  * { margin: 0; padding: 0; box-sizing: border-box; }
  html, body { width: 1200px; height: 697px; overflow: hidden; }
  body {
    background: var(--backdrop);
    font-family: "Source Sans 3", Arial, sans-serif;
    color: var(--ink);
    position: relative;
  }
  .sheet { position: absolute; background: var(--paper); box-shadow: 0 1px 3px rgba(0,0,0,.18); }

  .brand { display: flex; align-items: center; gap: 6px; font-weight: 700; color: var(--ink); white-space: nowrap; }
  .brand-dot { border-radius: 50%; background: var(--brand-red); flex: none; }

  /* Business card */
  .business-card { left: 24px; top: 314px; width: 161px; height: 111px; border-radius: 8px; overflow: hidden; }
  .business-card .brand { position: absolute; left: 10px; top: 10px; font-size: 8px; }
  .business-card .brand-dot { width: 14px; height: 14px; }
  .card-strip { position: absolute; right: 0; top: 0; width: 17px; height: 100%; background: var(--brand-red); }
  .card-person { position: absolute; right: 26px; top: 30px; text-align: right; white-space: nowrap; }
  .card-name { font-size: 11px; line-height: 1.1; color: var(--brand-red); font-weight: 600; }
  .card-title { font-size: 6.5px; line-height: 1.3; font-style: italic; color: var(--muted); }
  .card-contact { position: absolute; left: 10px; top: 66px; font-size: 5px; line-height: 1.35; color: var(--muted); }

  /* Letterhead */
  .letterhead { left: 216px; top: 34px; width: 432px; height: 636px; }
  .letterhead .brand { position: absolute; left: 50%; top: 22px; transform: translateX(-50%); font-size: 12px; }
  .letterhead .brand-dot { width: 26px; height: 26px; }
  .letterhead-web { position: absolute; right: 14px; top: 18px; font-size: 6px; color: var(--muted); }
  .letterhead-mark { position: absolute; left: 50%; top: 268px; transform: translateX(-50%); display: flex; align-items: center; gap: 12px; font-size: 24px; font-weight: 700; color: var(--faint); white-space: nowrap; }
  .letterhead-mark .brand-dot { width: 70px; height: 70px; background: var(--faint); }
  .letterhead-footer { position: absolute; left: 0; right: 0; bottom: 28px; display: flex; justify-content: center; gap: 22px; font-size: 7px; color: var(--ink); white-space: nowrap; }

  /* Envelope front */
  .envelope-front { left: 674px; top: 185px; width: 495px; height: 201px; }
  .envelope-front .brand { position: absolute; right: 14px; top: 12px; font-size: 8px; }
  .envelope-front .brand-dot { width: 18px; height: 18px; }
  .envelope-web { position: absolute; right: 14px; top: 36px; font-size: 6px; color: var(--muted); }
  .envelope-return { position: absolute; left: 0; right: 0; top: 135px; display: flex; justify-content: center; gap: 20px; font-size: 7px; white-space: nowrap; }

  /* Envelope back */
  .envelope-back { left: 674px; top: 408px; width: 495px; height: 250px; }
  .envelope-flap { position: absolute; left: 0; top: 0; width: 100%; height: 78px; }
  .envelope-seal { position: absolute; right: 14px; bottom: 14px; width: 22px; height: 22px; border-radius: 50%; background: var(--faint); }
</style>
</head>
<body>

<section class="sheet business-card">
  <div class="brand"><span class="brand-dot"></span>Norland Equity Partners</div>
  <div class="card-strip"></div>
  <div class="card-person">
    <p class="card-name">Tom Radcliffe</p>
    <p class="card-title">President</p>
  </div>
  <p class="card-contact">728 Maplewood Ave. Suite 310<br>Oak Terrace, CA 90418<br>Phone: 555-014-2290<br>tom@NorlandEquityPartners.com</p>
</section>

<section class="sheet letterhead">
  <div class="brand"><span class="brand-dot"></span>Norland Equity Partners</div>
  <p class="letterhead-web">www.NorlandEquityPartners.com</p>
  <div class="letterhead-mark"><span class="brand-dot"></span>Norland Equity Partners</div>
  <div class="letterhead-footer">
    <span>728 Maplewood Ave. Suite 310 Oak Terrace, CA 90418</span>
    <span>Email: tom@NorlandEquityPartners.com</span>
    <span>Phone: 555-014-2290</span>
  </div>
</section>

<section class="sheet envelope-front">
  <div class="brand"><span class="brand-dot"></span>Norland Equity Partners</div>
  <p class="envelope-web">www.NorlandEquityPartners.com</p>
  <div class="envelope-return">
    <span>728 Maplewood Ave. Suite 310 Oak Terrace, CA 90418</span>
    <span>Email: tom@NorlandEquityPartners.com</span>
    <span>Phone: 555-014-2290</span>
  </div>
</section>

<section class="sheet envelope-back">
  <svg class="envelope-flap" viewBox="0 0 495 78" preserveAspectRatio="none" aria-hidden="true">
    <rect x="0" y="0" width="495" height="10" fill="var(--lining)"/>
    <path d="M0 0 H495 V8 L440 70 Q436 76 428 76 H67 Q59 76 55 70 L0 8 Z" fill="var(--flap)"/>
  </svg>
  <span class="envelope-seal"></span>
</section>

</body>
</html>
```